ラベルのイメ―ジ
・高級感
・安心感
・品質(GMP認定工場による生産)

※NMNの化学式や、DNA螺旋などをイメージするようなイラストも良いと考えています。必須ではありません。

ターゲット層は以下を想定しています
性別:どちらもあると考えていますが、パッケージラベルは男性向けと想定しています
収入:余裕のある方
年齢:30-60歳
サイズ:W65㎜×H80㎜
カラー:黒字にゴールド
赤系、青系、無彩色系、ゴールド
写真のパッケージは、白ですが、実物は同じ物の黒を想定しています。ファイル「ラベルのサンプル画像.jpg」は、他社製品で、イメージの近いものを選んでいます。

要件をそろえたすばらしいデザインです。
ありがとうございます。

この度は、多くの方よりご提案をいただきました。まことにありがとうございます。
今後も新製品や、製品説明資料などでおご依頼の機会が有るかと思います。
その際もよろしくお願いします。

```html
<!DOCTYPE html>
<html lang="ja">
<head>
<meta charset="UTF-8">
<title>毎日の活力 NMN ラベル</title>
<link rel="stylesheet" href="https://fonts.googleapis.com/css2?family=Noto+Sans+JP:wght@500;700&family=Josefin+Sans:ital,wght@0,400;0,600;1,400&display=swap">
<style>
  :root {
    --label-black: #0b0b0b;
    --label-ink: #161616;
    --gold-light: #f3dc9a;
    --gold: #c9a24a;
    --gold-deep: #8a6622;
    --white: #f5f5f2;
  }
  * { margin: 0; padding: 0; box-sizing: border-box; }
  html, body {
    width: 802px;
    height: 1200px;
    overflow: hidden;
    background: var(--label-black);
  }
  .label {
    position: relative;
    width: 802px;
    height: 1200px;
    background: linear-gradient(160deg, var(--label-ink) 0%, var(--label-black) 60%);
    overflow: hidden;
  }
  .label__title {
    position: absolute;
    left: 62px;
    top: 190px;
    font-family: "Noto Sans JP", sans-serif;
    font-weight: 700;
    font-size: 66px;
    letter-spacing: 4px;
    color: var(--white);
    line-height: 1;
  }
  .label__name {
    position: absolute;
    left: 56px;
    top: 290px;
    font-family: "Josefin Sans", sans-serif;
    font-weight: 400;
    font-size: 176px;
    letter-spacing: 2px;
    line-height: 1;
    background: linear-gradient(180deg, var(--gold-light) 0%, var(--gold) 55%, var(--gold-deep) 100%);
    -webkit-background-clip: text;
    background-clip: text;
    color: transparent;
  }
  .label__ingredient {
    position: absolute;
    left: 64px;
    top: 640px;
    font-family: "Josefin Sans", sans-serif;
    font-style: italic;
    font-weight: 400;
    font-size: 34px;
    line-height: 1.3;
    letter-spacing: 3px;
    color: var(--gold);
  }
  .label__count {
    position: absolute;
    left: 64px;
    top: 900px;
    font-family: "Josefin Sans", sans-serif;
    font-weight: 600;
    font-size: 30px;
    letter-spacing: 1px;
    color: var(--white);
  }
  .label__helix {
    position: absolute;
    left: 550px;
    top: 60px;
    width: 210px;
    height: 1080px;
  }
</style>
</head>
<body>
  <main class="label">
    <h1 class="label__title">毎日の活力</h1>
    <p class="label__name">NMN</p>
    <p class="label__ingredient">nicotinamide<br>mononucleotide</p>
    <p class="label__count">90 tablets</p>
    <svg class="label__helix" viewBox="0 0 210 1080" role="img" aria-label="金色に輝くDNA二重螺旋のイラスト">
      <defs>
        <linearGradient id="helixGold" x1="0" y1="0" x2="1" y2="1">
          <stop offset="0" stop-color="#f3dc9a" stop-opacity="0.5"/>
          <stop offset="0.5" stop-color="#c9a24a" stop-opacity="0.42"/>
          <stop offset="1" stop-color="#8a6622" stop-opacity="0.32"/>
        </linearGradient>
      </defs>
      <rect x="0" y="0" width="210" height="1080" rx="105" fill="url(#helixGold)"/>
    </svg>
  </main>
</body>
</html>
```